Business Card Design

We need a business card design for a new dental practice in Brisbane. I'd like the basic details and logo on one side and appointment schedule on the other side. It is based in CBD office area and would prefer a professional and modern design.
Target Market(s)
20-60 years old office workers and residents with high education levels
Industry/Entity Type
Dental
Contact Information for Business Card
Harbourlight Dental
Dr Marcus Lindqvist
Principal Dentist
07 3194 6627
admin@harbourlightdentistry.example.au
www.harbourlightdentistry.example.au
S27, Level 3, Ferndale North Tower, 318 Gorrick St, Alderwood Heights, QLD 4118

```html
<!DOCTYPE html>
<html lang="en">
<head>
<meta charset="utf-8">
<title>Harbourlight Dental – Business Card</title>
<link href="https://fonts.googleapis.com/css2?family=Quicksand:wght@500&family=Source+Sans+3:wght@400;700&display=swap" rel="stylesheet">
<style>
  :root {
    --backdrop: #d4d5d7;
    --card: #ffffff;
    --brand-blue: #4fb2e3;
    --ink: #14202b;
    --muted: #7a7a7a;
    --divider: #e9eaeb;
  }
  html, body {
    margin: 0;
    width: 1200px;
    height: 1200px;
    overflow: hidden;
    background: var(--backdrop);
    font-family: "Source Sans 3", "Helvetica Neue", Arial, sans-serif;
  }
  .canvas { position: relative; width: 1200px; height: 1200px; }
  .card {
    position: absolute;
    left: 216px;
    width: 764px;
    background: var(--card);
    overflow: hidden;
  }
  .card--front { top: 130px; height: 460px; }
  .card--back { top: 600px; height: 461px; }
  .gap-line { position: absolute; left: 216px; top: 590px; width: 764px; height: 10px; background: var(--divider); }
  .band { position: absolute; left: 0; width: 100%; background: var(--brand-blue); }
  .card--front .band { top: 248px; height: 212px; }
  .card--back .band { top: 0; height: 214px; }
  .abs { position: absolute; white-space: nowrap; }

  .wordmark {
    font-family: "Quicksand", "Century Gothic", sans-serif;
    font-weight: 500;
    font-size: 32px;
    color: var(--ink);
    display: flex;
    align-items: center;
    gap: 10px;
  }
  .wordmark__dot { width: 16px; height: 16px; border-radius: 50%; background: var(--brand-blue); }
  .wordmark__dot--light { background: #fff; }
  .card--front .wordmark { right: 40px; top: 138px; }
  .card--back .wordmark { left: 30px; top: 108px; }

  .person__name { left: 73px; top: 346px; font-size: 26px; font-weight: 700; color: var(--ink); }
  .person__role { left: 73px; top: 379px; font-size: 21px; color: #fff; }

  .contact { left: 378px; color: #fff; font-size: 19px; line-height: 27px; }
  .contact__row { display: flex; align-items: flex-start; gap: 10px; }
  .contact__row svg { flex: none; margin-top: 5px; }
  .contact--address { top: 258px; }
  .contact--lines { top: 353px; }

  .back-url { left: 30px; top: 150px; font-size: 21px; color: #fff; }

  .appointment { left: 382px; top: 274px; color: var(--muted); }
  .appointment__title { font-size: 21px; line-height: 28px; margin: 0 0 4px; }
  .appointment__row { font-size: 18px; line-height: 26px; margin: 0 0 0 31px; display: flex; align-items: center; gap: 2px; }
  .box { display: inline-block; width: 14px; height: 14px; border: 1.5px solid var(--muted); margin: 0 6px 0 3px; }
  .blank { display: inline-block; border-bottom: 1.5px solid var(--muted); height: 15px; }
</style>
</head>
<body>
<div class="canvas">
  <section class="card card--front">
    <div class="wordmark abs"><span class="wordmark__dot"></span>Harbourlight Dental</div>
    <div class="band"></div>
    <div class="person__name abs">Dr Marcus Lindqvist</div>
    <div class="person__role abs">Principal Dentist</div>

    <div class="contact contact--address abs">
      <div class="contact__row">
        <svg width="18" height="18" viewBox="0 0 18 18"><circle cx="9" cy="9" r="9" fill="#fff"/><path d="M4 9.5 9 5l5 4.5M5.5 8.5V13h7V8.5" fill="none" stroke="#4fb2e3" stroke-width="1.6"/></svg>
        <div>S27, Level 3, Ferndale North Tower<br>318 Gorrick St, Alderwood Heights<br>QLD 4118</div>
      </div>
    </div>

    <div class="contact contact--lines abs">
      <div class="contact__row">
        <svg width="18" height="18" viewBox="0 0 18 18"><rect width="18" height="18" rx="4" fill="#fff"/><rect x="6" y="3.5" width="6" height="11" rx="1" fill="none" stroke="#4fb2e3" stroke-width="1.5"/></svg>
        <div>07 3194 6627</div>
      </div>
      <div class="contact__row">
        <svg width="18" height="18" viewBox="0 0 18 18"><circle cx="9" cy="9" r="8.2" fill="none" stroke="#fff" stroke-width="1.5"/><rect x="4.5" y="6" width="9" height="6.5" fill="none" stroke="#fff" stroke-width="1.3"/><path d="M4.5 6 9 10l4.5-4" fill="none" stroke="#fff" stroke-width="1.3"/></svg>
        <div>admin@harbourlightdentistry.example.au</div>
      </div>
      <div class="contact__row">
        <svg width="18" height="18" viewBox="0 0 18 18" fill="none" stroke="#fff" stroke-width="1.3"><circle cx="9" cy="9" r="8"/><ellipse cx="9" cy="9" rx="3.5" ry="8"/><path d="M1 9h16M2.5 5h13M2.5 13h13"/></svg>
        <div>www.harbourlightdentistry.example.au</div>
      </div>
    </div>
  </section>

  <div class="gap-line"></div>

  <section class="card card--back">
    <div class="band"></div>
    <div class="wordmark abs"><span class="wordmark__dot wordmark__dot--light"></span>Harbourlight Dental</div>
    <div class="back-url abs">www.harbourlightdentistry.example.au</div>

    <div class="appointment abs">
      <p class="appointment__title">Next Appointment:</p>
      <p class="appointment__row">Mon<span class="box"></span>Tue<span class="box"></span>Wed<span class="box"></span>Thur<span class="box"></span></p>
      <p class="appointment__row">Date:<span class="blank" style="width:84px"></span>at<span class="blank" style="width:50px"></span>AM<span class="box"></span>&nbsp;PM<span class="box"></span></p>
    </div>
  </section>
</div>
</body>
</html>
```